Flyer for Cafe

We need a flyer to promote our menu..
I'd like to say:
-Burgers made to order
-Fresh Sandwiches and wraps daily
-Amazing coffee
-Hot Chips available (french fries.. we call them chips in Australia)
I have attached our logo below, and I have also attached a flyer that i like the look of..am wanting something similar.
Flyer to be one sided on A4 Paper
UPDATE:
I forgot to add our location...if we can put
"Located at The Harrowmere Uni Hospital"
"Open from 6am till 4pm. Monday - Friday"
Along the bottom of the flyer, with the contact details, can we please add an pixlane icon and a like us on Chatterbook icon.
We are a cafe at a Hospital, so we target doctors, nurses.
We are also next to a university, so we are trying to attract students also
Cafe

```html
<!DOCTYPE html>
<html lang="en">
<head>
<meta charset="utf-8">
<title>Ward Rounds Canteen – Cafe Flyer</title>
<link rel="stylesheet" href="https://fonts.googleapis.com/css2?family=Playfair+Display:wght@400;700&family=Marcellus&display=swap">
<style>
  :root {
    --brown-deep: #2e1414;
    --brown: #3d1d1d;
    --label-bg: #46201f;
    --gold-light: #f3e9a6;
    --gold: #d9c37a;
    --orange: #e27d1e;
    --label-text: #e9a15a;
    --grey-text: #c8b9b7;
    --red: #e01d2f;
  }
  * { margin: 0; padding: 0; box-sizing: border-box; }
  html, body { width: 848px; height: 1200px; overflow: hidden; background: var(--brown-deep); }
  .flyer {
    position: relative;
    width: 848px;
    height: 1200px;
    overflow: hidden;
    background: var(--brown);
    font-family: "Playfair Display", serif;
  }
  .backdrop { position: absolute; inset: 0; width: 848px; height: 1200px; }

  .menu-card {
    position: absolute;
    width: 291px;
    background: var(--label-bg);
    box-shadow: 0 2px 6px rgba(0,0,0,.35);
  }
  .menu-card .caption {
    height: 40px;
    line-height: 40px;
    text-align: center;
    color: var(--label-text);
    font-family: "Playfair Display", serif;
    font-size: 22px;
    font-weight: 400;
  }
  .menu-card .photo { height: 161px; }
  .card-coffee { left: 476px; top: 131px; }
  .card-coffee .photo { background: linear-gradient(135deg, #7a7672, #d8d4cf 50%, #4a4643); }
  .card-sandwich { left: 114px; top: 283px; }
  .card-sandwich .photo { background: radial-gradient(ellipse at 50% 55%, #b98a55 0%, #6a4a2a 40%, #000 72%); }
  .card-burger { left: 437px; top: 427px; }
  .card-burger .photo { background: radial-gradient(ellipse at 45% 50%, #c88a3a 0%, #5b3418 45%, #0a0504 80%); }
  .card-chips { left: 18px; top: 564px; }
  .card-chips .photo { background: radial-gradient(ellipse at 45% 55%, #f0c25e 0%, #d9a74a 35%, #e9e7e4 60%, #263247 100%); }

  .beans {
    position: absolute;
    left: 14px; top: 1040px;
    width: 180px; height: 78px;
    border-radius: 50%;
    background: radial-gradient(ellipse at 50% 50%, #4a2a22 0%, #3a1e1a 55%, rgba(61,29,29,0) 75%);
  }

  .hours {
    position: absolute;
    left: 180px; top: 968px;
    width: 350px;
    text-align: center;
    color: var(--grey-text);
    font-weight: 700;
    font-size: 28px;
    line-height: 1.2;
  }
  .hours .days { display: block; margin-top: 14px; font-size: 36px; }

  .location {
    position: absolute;
    left: 22px; top: 1102px;
    color: var(--orange);
    font-weight: 700;
    font-size: 46px;
    line-height: 1;
    white-space: nowrap;
  }

  .brand {
    position: absolute;
    left: 545px; top: 930px;
    display: flex;
    align-items: center;
    gap: 14px;
  }
  .brand .mark {
    width: 58px; height: 58px;
    border-radius: 50%;
    background: var(--red);
    flex: none;
  }
  .brand .name {
    color: var(--red);
    font-weight: 700;
    font-size: 34px;
    line-height: 1.05;
  }

  .social {
    position: absolute;
    left: 600px; top: 1022px;
    list-style: none;
    color: var(--grey-text);
    font-size: 20px;
    line-height: 1;
  }
  .social li { display: flex; align-items: center; gap: 10px; margin-bottom: 14px; }
  .social .dot {
    width: 22px; height: 22px;
    border-radius: 50%;
    background: var(--grey-text);
    flex: none;
  }
</style>
</head>
<body>
<main class="flyer">
  <svg class="backdrop" viewBox="0 0 848 1200" aria-hidden="true">
    <defs>
      <linearGradient id="gold-field" x1="0" y1="0" x2="1" y2="1">
        <stop offset="0" stop-color="#d8c47e"/>
        <stop offset=".45" stop-color="#f4eaa8"/>
        <stop offset="1" stop-color="#cdb46c"/>
      </linearGradient>
      <linearGradient id="silver-band" x1="0" y1="0" x2="1" y2="0">
        <stop offset="0" stop-color="#8c7f7f"/>
        <stop offset=".5" stop-color="#f4f1f1"/>
        <stop offset="1" stop-color="#9a8e8e"/>
      </linearGradient>
      <path id="arc-coffee" d="M228 130 C 320 80, 420 45, 520 30"/>
      <path id="arc-food" d="M590 22 C 680 20, 760 35, 830 55"/>
    </defs>

    <path d="M0 300 C 220 200, 430 110, 610 80 C 720 62, 800 75, 848 95 L848 560 C 700 620, 520 700, 330 760 C 200 800, 90 830, 0 850 Z" fill="url(#gold-field)"/>

    <path d="M0 300 C 220 200, 430 110, 610 80 C 720 62, 800 75, 848 95" fill="none" stroke="url(#silver-band)" stroke-width="5"/>
    <path d="M0 330 C 200 245, 380 175, 560 145" fill="none" stroke="#5a2d2b" stroke-width="3" opacity=".6"/>

    <path d="M0 850 C 200 805, 420 745, 600 680 C 700 645, 790 610, 848 590" fill="none" stroke="#221010" stroke-width="26"/>
    <path d="M0 870 C 210 830, 430 770, 620 705 C 720 672, 800 640, 848 622" fill="none" stroke="url(#silver-band)" stroke-width="9"/>
    <path d="M0 895 C 220 860, 450 800, 640 735 C 740 702, 810 676, 848 662" fill="none" stroke="#241111" stroke-width="14"/>
    <path d="M0 915 C 230 885, 460 830, 650 765 C 750 732, 815 708, 848 696" fill="none" stroke="url(#silver-band)" stroke-width="4" opacity=".85"/>
    <path d="M0 960 C 240 930, 470 880, 660 815 C 760 780, 820 758, 848 748" fill="none" stroke="#4b2524" stroke-width="6" opacity=".7"/>

    <g transform="translate(106 94)">
      <circle r="55" fill="#f2c230"/>
      <circle r="46" fill="#f8e08a"/>
      <circle r="44" fill="none" stroke="#8a2d1c" stroke-width="1.5"/>
      <text y="-10" text-anchor="middle" font-family="Playfair Display, serif" font-weight="700" font-size="22" fill="#b5271b" transform="rotate(-15)">10 %</text>
      <text y="12" text-anchor="middle" font-family="Playfair Display, serif" font-weight="700" font-size="14" fill="#b5271b" transform="rotate(-15)">Student</text>
      <text y="30" text-anchor="middle" font-family="Playfair Display, serif" font-weight="700" font-size="14" fill="#b5271b" transform="rotate(-15)">Discount</text>
    </g>

    <text font-family="Marcellus, serif" font-size="28" fill="#e27d1e">
      <textPath href="#arc-coffee">Come for the COFFEE</textPath>
    </text>
    <text font-family="Marcellus, serif" font-size="28" fill="#e27d1e">
      <textPath href="#arc-food">Stay for the FOOD</textPath>
    </text>
  </svg>

  <section class="menu-card card-coffee">
    <h2 class="caption">Amazing</h2>
    <div class="photo" role="img" aria-label="Two cups of latte with latte art on saucers"></div>
    <p class="caption">Coffee</p>
  </section>

  <section class="menu-card card-sandwich">
    <h2 class="caption">Fresh Sandwiches</h2>
    <div class="photo" role="img" aria-label="A fresh sandwich and halved wraps"></div>
    <p class="caption">and Wraps daily</p>
  </section>

  <section class="menu-card card-burger">
    <h2 class="caption">Burgers</h2>
    <div class="photo" role="img" aria-label="A cheeseburger with lettuce and tomato beside chips"></div>
    <p class="caption">made to order</p>
  </section>

  <section class="menu-card card-chips">
    <h2 class="caption">HOT Chips</h2>
    <div class="photo" role="img" aria-label="A white bowl of hot chips"></div>
    <p class="caption">available</p>
  </section>

  <div class="beans" role="img" aria-label="Roasted coffee beans"></div>

  <p class="hours">Open from 6am till 4pm<span class="days">Monday - Friday</span></p>

  <div class="brand">
    <span class="mark"></span>
    <span class="name">Ward Rounds<br>Canteen</span>
  </div>

  <ul class="social">
    <li><span class="dot"></span>pixlane</li>
    <li><span class="dot"></span>Like us on Chatterbook</li>
  </ul>

  <p class="location">Harrowmere Uni hospital</p>
</main>
</body>
</html>
```